Wine Bottle Lable

Want a unique, simple but elegant, label for a wine bottle. I want to use the letters "TWG" in the design which is a moniker for my last name "Tallwidge". The letters TWG do not have to be juxtaposed together so that it is recognizable, or they could be something like T-WG, WG-T, TGW T-WG-T, etc. The X could be totally separated from the NO, or otherwise. The wine is a white wine in a clear bottle. I need Adobe Illustrator files so I can add the wine varietal, year, alcohol content. The label should be 4" wide and 5" tall.

Colors

Designer to choose colors to be used in the design.

Requirements
Nice to have
• outstanding but simple graphics

```html
<!DOCTYPE html>
<html lang="en">
<head>
<meta charset="utf-8">
<title>TGW Reserve Chardonnay – Label Variants</title>
<link rel="stylesheet" href="https://fonts.googleapis.com/css2?family=Bodoni+Moda:wght@400;500&family=Pinyon+Script&family=Source+Sans+3:wght@400&display=swap">
<style>
  :root {
    --backdrop-light: #c3c9c7;
    --backdrop-dark: #5b6564;
    --label-black: #000000;
    --label-green: #062a0c;
    --swirl-black-a: #020604;
    --swirl-black-b: #0a2412;
    --swirl-green-a: #06290d;
    --swirl-green-b: #0d3a19;
    --gold: #d6a21f;
    --gold-text: #e3ae2a;
    --white: #ffffff;
  }
  * { margin: 0; padding: 0; box-sizing: border-box; }
  html, body {
    width: 1200px;
    height: 822px;
    overflow: hidden;
  }
  body {
    position: relative;
    background: radial-gradient(ellipse 70% 75% at 50% 50%, var(--backdrop-light) 0%, #9aa3a1 55%, var(--backdrop-dark) 100%);
  }
  .label {
    position: absolute;
    top: 137px;
    width: 438px;
    height: 548px;
    overflow: hidden;
    text-align: center;
  }
  .label--black { left: 139px; background: var(--label-black); }
  .label--green { left: 620px; background: var(--label-green); }

  .label__swirl {
    position: absolute;
    inset: 0;
  }
  .label--black .label__swirl {
    background: radial-gradient(circle at 55% 45%, var(--swirl-black-b) 0%, var(--swirl-black-a) 75%);
  }
  .label--green .label__swirl {
    background: radial-gradient(circle at 55% 45%, var(--swirl-green-b) 0%, var(--swirl-green-a) 75%);
  }

  .label__brand {
    position: absolute;
    top: 40px;
    left: 0;
    right: 0;
    font-family: "Bodoni Moda", serif;
    font-weight: 500;
    font-size: 122px;
    line-height: 1;
    letter-spacing: 2px;
    color: var(--gold);
  }
  .label__vintage {
    position: absolute;
    top: 290px;
    left: 0;
    right: 0;
    font-family: "Bodoni Moda", serif;
    font-weight: 400;
    font-size: 44px;
    line-height: 1;
    color: var(--white);
  }
  .label__varietal {
    position: absolute;
    top: 333px;
    left: 0;
    right: 0;
    font-family: "Pinyon Script", cursive;
    font-size: 58px;
    line-height: 1;
    color: var(--white);
  }
  .label__tier,
  .label__estate {
    position: absolute;
    left: 0;
    right: 0;
    font-family: "Bodoni Moda", serif;
    font-weight: 500;
    font-size: 26px;
    line-height: 1;
    color: var(--gold-text);
  }
  .label__tier { top: 428px; }
  .label__estate { top: 458px; }

  .label__volume,
  .label__abv {
    position: absolute;
    font-family: "Source Sans 3", sans-serif;
    color: var(--white);
    line-height: 1;
  }
  .label__volume { left: 18px; bottom: 18px; font-size: 24px; }
  .label__abv { right: 18px; bottom: 20px; font-size: 19px; }
</style>
</head>
<body>
  <section class="label label--black">
    <div class="label__swirl" role="img" aria-label="Decorative pattern of interlocking green arcs"></div>
    <div class="label__brand">TGW</div>
    <div class="label__vintage">2012</div>
    <div class="label__varietal">Chardonnay</div>
    <div class="label__tier">Reserve</div>
    <div class="label__estate">Wine Valley Vineyard</div>
    <div class="label__volume">750ml</div>
    <div class="label__abv">Alc. 14% by Vol.</div>
  </section>

  <section class="label label--green">
    <div class="label__swirl" role="img" aria-label="Decorative pattern of interlocking green arcs"></div>
    <div class="label__brand">TGW</div>
    <div class="label__vintage">2012</div>
    <div class="label__varietal">Chardonnay</div>
    <div class="label__tier">Reserve</div>
    <div class="label__estate">Wine Valley Vineyard</div>
    <div class="label__volume">750ml</div>
    <div class="label__abv">Alc. 14% by Vol.</div>
  </section>
</body>
</html>
```